Website for The Velvet Pathfinder

We need an impressive e-commerce website for our newly launched business "The Velvet Pathfinder".
The Velvet Pathfinder searches store-front and online retailers for diamond engagement rings according to the client's specified requirements. We want to save people time by doing the shopping around for them.
We can relate to, and we love, www.corvaline.com
Like corvaline.com, we want to offer website visitors a quick run-down on how the process works, then offer them to elect a service package and pay for that package on the spot.
Content pages:
HOME
HOW IT WORKS
DIAMOND GALLERY
ABOUT
FAQs
CONTACT
Inclusions: Our logo and Facebook and Instagram buttons
We want to be able to easily edit this website, We want it to display well on iPhone and android, We want it to be clean and striking.
Like our logo, we want our website to embody elegant masculinity.
Target Market(s)
Men in market for diamond ring purchase $5k - $50k
Industry/Entity Type
Business
Number of Pages Required
5+ page
Font styles to use
Look and feel

```html
<!DOCTYPE html>
<html lang="en">
<head>
<meta charset="utf-8">
<title>The Velvet Pathfinder</title>
<link href="https://fonts.googleapis.com/css2?family=Cinzel:wght@400;500&family=Roboto+Slab:wght@300;400;700&family=Noto+Serif:ital,wght@1,400;1,700&display=swap" rel="stylesheet">
<style>
:root{
  --ink:#4a4a4a;
  --muted:#777;
  --soft:#9a9a9a;
  --gold:#c8a84b;
  --band:#ebebeb;
  --page:#f7f7f7;
  --hero-dark:#141414;
  --white:#fff;
  --button:#8b8b8b;
}
*{margin:0;padding:0;box-sizing:border-box}
html,body{width:1200px;height:1000px;overflow:hidden;background:var(--white)}
body{position:relative;font-family:"Roboto Slab",serif;color:var(--ink)}

.site-header{position:absolute;left:0;top:0;width:1200px;height:157px;background:var(--white)}
.brand{position:absolute;left:48px;top:58px;width:150px;text-align:center;font-family:"Cinzel",serif;font-size:15px;line-height:19px;color:#5a5a5a;letter-spacing:.5px}
.brand-dot{display:block;width:34px;height:34px;border-radius:50%;background:#9a9a9a;margin:-44px auto 12px}
.utility{position:absolute;top:22px;font-size:13px;font-weight:300;color:var(--ink);display:flex;align-items:center;gap:6px;white-space:nowrap}
.utility svg{width:11px;height:11px}
.utility .caret{width:7px;height:7px}
.main-nav{position:absolute;left:298px;top:76px;font-size:19px;font-weight:300;color:#555}
.main-nav a{color:inherit;text-decoration:none;position:absolute;white-space:nowrap}
.cart{position:absolute;left:1046px;top:69px;width:35px;height:35px;border-radius:50%;background:var(--gold)}
.cart svg{position:absolute;left:9px;top:8px}
.cart-count{position:absolute;left:1071px;top:67px;width:18px;height:18px;border-radius:50%;background:#e8e8ee;font-size:11px;text-align:center;line-height:18px;color:#555}
.cart-total{position:absolute;left:1098px;top:80px;font-size:15px;font-weight:300;color:#aaa}

.hero{position:absolute;left:0;top:157px;width:1200px;height:534px;background:radial-gradient(ellipse at 75% 45%,#3a3a3a 0%,#222 45%,var(--hero-dark) 100%)}
.hero-photo{position:absolute;left:0;top:0;width:620px;height:534px;background:linear-gradient(90deg,#3b2a22 0%,#8a6a58 35%,#c9a08a 55%,#6a4a3c 80%,rgba(20,20,20,0) 100%)}
.hero-copy{position:absolute;left:440px;top:176px;width:800px;text-align:center;color:var(--white);white-space:nowrap}
.hero-title{font-family:"Cinzel",serif;font-weight:400;letter-spacing:1px}
.hero-title .small{display:block;font-size:36px;line-height:44px}
.hero-title .large{display:block;font-size:43px;line-height:52px}
.hero-sub{margin-top:14px;font-size:18px;font-weight:700;letter-spacing:.2px}
.hero-button{position:absolute;left:727px;top:347px;width:234px;height:60px;background:var(--button);border:1px solid #bdbdbd;color:var(--white);font-family:"Cinzel",serif;font-size:21px;letter-spacing:1px;text-align:center;line-height:58px;white-space:nowrap}

.shape-band{position:absolute;left:0;top:691px;width:1196px;height:115px;background:var(--band)}
.shape-title{position:absolute;left:18px;top:25px;font-family:"Cinzel",serif;font-weight:400;color:#333;text-align:center;width:206px;white-space:nowrap}
.shape-title .small{display:block;font-size:26px;line-height:28px}
.shape-title .large{display:block;font-size:34px;line-height:38px}
.shape{position:absolute;background:radial-gradient(circle,#ffffff 0%,#cfd6e2 55%,#9aa4b4 100%)}

.intro{position:absolute;left:0;top:806px;width:1200px;height:194px;background:var(--page)}
.ring-photo{position:absolute;left:50px;top:150px;width:142px;height:60px;border-radius:40px 40px 0 0;background:linear-gradient(180deg,#d8d8d8,#8a8a8a)}
.intro-heading{position:absolute;left:370px;top:108px;width:694px;display:flex;align-items:center;gap:6px;font-family:"Noto Serif",serif;font-style:italic;font-weight:400;font-variant:small-caps;color:#8e8e8e;font-size:36px;white-space:nowrap}
.intro-heading .rule{flex:1;height:2px;background:#aaa}
.intro-heading strong{font-weight:700;color:#8a8a8a}
.intro-text{position:absolute;left:363px;top:163px;font-family:"Noto Serif",serif;font-style:italic;font-size:20px;color:var(--soft);white-space:nowrap}
</style>
</head>
<body>

<header class="site-header">
  <div class="brand"><span class="brand-dot"></span>THE VELVET<br>PATHFINDER</div>

  <div class="utility" style="left:652px">
    <svg viewBox="0 0 12 12"><path d="M2 1l2 0 1 3-1.5 1a7 7 0 0 0 3.5 3.5L8 7l3 1v2c0 .6-.4 1-1 1A9 9 0 0 1 1 2c0-.6.4-1 1-1z" fill="#444"/></svg>
    (00)-987-654-321
  </div>
  <div class="utility" style="left:789px">
    <svg viewBox="0 0 12 12"><rect x="1" y="2.5" width="10" height="7" fill="none" stroke="#444"/><path d="M1 2.5l5 4 5-4" fill="none" stroke="#444"/></svg>
    hello@pathfind.co
  </div>
  <div class="utility" style="left:950px">English
    <svg class="caret" viewBox="0 0 8 8"><path d="M1 2.5l3 3 3-3" fill="none" stroke="#444"/></svg></div>
  <div class="utility" style="left:1035px">USD
    <svg class="caret" viewBox="0 0 8 8"><path d="M1 2.5l3 3 3-3" fill="none" stroke="#444"/></svg></div>
  <div class="utility" style="left:1101px">Login</div>

  <nav class="main-nav">
    <a style="left:0">HOME</a>
    <a style="left:85px">HOW IT WORKS</a>
    <a style="left:254px">DIAMOND GALLERY</a>
    <a style="left:463px">ABOUT</a>
    <a style="left:556px">FAQS</a>
    <a style="left:631px">CONTACT</a>
  </nav>

  <div class="cart">
    <svg width="17" height="18" viewBox="0 0 17 18"><rect x="1.5" y="6" width="14" height="11" fill="none" stroke="#fff" stroke-width="1.5"/><path d="M5 6V4a3.5 3.5 0 0 1 7 0v2" fill="none" stroke="#fff" stroke-width="1.5"/></svg>
  </div>
  <div class="cart-count">2</div>
  <div class="cart-total">$25.00</div>
</header>

<section class="hero">
  <div class="hero-photo" role="img" aria-label="Smiling woman wearing a diamond ring, drop earrings and necklace"></div>
  <div class="hero-copy">
    <h1 class="hero-title"><span class="small">THE EASIEST WAY TO</span><span class="large">SEARCH FOR DIAMONDS</span></h1>
    <p class="hero-sub">COLLECTION OF BEAUTIFUL DIAMONDS.&nbsp; STARTING FROM $79.</p>
  </div>
  <a class="hero-button">FIND YOUR STYLE</a>
</section>

<section class="shape-band">
  <h2 class="shape-title"><span class="small">SEARCH FOR</span><span class="large">DIAMONDS</span></h2>
  <div class="shape" role="img" aria-label="Asscher cut diamond" style="left:252px;top:27px;width:60px;height:60px"></div>
  <div class="shape" role="img" aria-label="Cushion cut diamond" style="left:361px;top:27px;width:58px;height:58px;border-radius:14px"></div>
  <div class="shape" role="img" aria-label="Emerald cut diamond" style="left:466px;top:26px;width:44px;height:62px"></div>
  <div class="shape" role="img" aria-label="Heart shaped diamond" style="left:557px;top:27px;width:60px;height:58px;border-radius:50% 50% 50% 50%/40% 40% 60% 60%"></div>
  <div class="shape" role="img" aria-label="Marquise cut diamond" style="left:666px;top:27px;width:30px;height:62px;border-radius:50%"></div>
  <div class="shape" role="img" aria-label="Oval cut diamond" style="left:731px;top:27px;width:40px;height:60px;border-radius:50%"></div>
  <div class="shape" role="img" aria-label="Pear shaped diamond" style="left:814px;top:27px;width:34px;height:62px;border-radius:50% 50% 50% 50%/30% 30% 70% 70%"></div>
  <div class="shape" role="img" aria-label="Princess cut diamond" style="left:889px;top:26px;width:59px;height:59px"></div>
  <div class="shape" role="img" aria-label="Radiant cut diamond" style="left:987px;top:25px;width:58px;height:58px;border-radius:12px"></div>
  <div class="shape" role="img" aria-label="Round brilliant diamond" style="left:1081px;top:22px;width:60px;height:60px;border-radius:50%"></div>
</section>

<section class="intro">
  <div class="ring-photo" role="img" aria-label="Diamond engagement ring"></div>
  <h2 class="intro-heading"><span class="rule"></span>Find your <strong>perfect diamond</strong><span class="rule"></span></h2>
  <p class="intro-text">Choosing your diamond is an exciting process. Carat, cut, clarity, and colour</p>
</section>

</body>
</html>
```